Entertainer/Dancer Business Cards

Devon Marsh is an up and coming entertainer from Baltimore, Maryland currently relocating to Los Angeles, California for a dance opportunity at the renowned Ruthie Calder Dance Studio.
This young man needs to promote himself and his skills in a populous and competitive city.
Hopefully, this card will set him apart from the tons of entertainers in L.A.
It will passed out to fellow entertainers, agents, and random people looking for talent.

I have uploaded an image of the dancer, it is not necessary to use this image; however it is in PSD format if one should decide to incorporate it somehow and would like to make changes.

Industry/Entity Type

Business

Contact Information for Business Card

Devon Marsh
(line 1) Dancer Choreographer Instructor Singer/Songwriter
(line 2) Ballet-Modern-Urban
devonmarsh00@fernpost.com
410-582-7146

Requirements
Nice to have

• Open to an all typography card.
Should not have
• No logo; just name: Devon Marsh
Devon is a guy (in case you were wondering :D )
Please no ballet/pointe shoes in design

```html
<!DOCTYPE html>
<html lang="en">
<head>
<meta charset="utf-8">
<title>Devon Marsh – Business Card</title>
<link href="https://fonts.googleapis.com/css2?family=Quicksand:wght@300;400;500&display=swap" rel="stylesheet">
<style>
  :root {
    --backdrop: #2b2b2b;
    --card: #ffffff;
    --ink: #1c1c1c;
    --accent: #e0401a;
    --skin-dark: #5a1f0c;
    --skin-mid: #a8431c;
    --skin-light: #d0763d;
  }
  html, body {
    margin: 0;
    width: 1200px;
    height: 1000px;
    overflow: hidden;
    background: var(--backdrop);
    font-family: "Quicksand", sans-serif;
  }
  .card {
    position: absolute;
    left: 100px;
    top: 214px;
    width: 1000px;
    height: 571px;
    background: var(--card);
    border-radius: 10px;
    overflow: hidden;
    box-shadow: 0 20px 50px rgba(0,0,0,0.45);
  }
  .card__accent-line {
    position: absolute;
    left: 0;
    top: 0;
    width: 1000px;
    height: 571px;
  }
  .card__portrait {
    position: absolute;
    left: 60px;
    top: 40px;
    width: 250px;
    height: 430px;
  }
  .card__details {
    position: absolute;
    left: 340px;
    top: 150px;
    color: var(--ink);
  }
  .card__name {
    margin: 0 0 0 20px;
    font-weight: 400;
    font-size: 48px;
    line-height: 1.1;
    letter-spacing: 0.5px;
    padding: 0 12px 4px 4px;
    border-bottom: 2px solid var(--ink);
    display: inline-block;
  }
  .card__roles {
    margin: 10px 0 0 0;
    font-weight: 300;
    font-size: 19px;
    letter-spacing: 0.3px;
    white-space: nowrap;
  }
  .card__styles {
    margin: 12px 0 0 0;
    font-weight: 300;
    font-size: 18px;
  }
  .card__contact {
    list-style: none;
    margin: 48px 0 0 24px;
    padding: 0;
    font-weight: 400;
    font-size: 19px;
  }
  .card__contact li {
    display: flex;
    align-items: center;
    gap: 12px;
    margin-bottom: 10px;
  }
  .card__icon {
    width: 18px;
    height: 18px;
    fill: var(--ink);
    flex: none;
  }
</style>
</head>
<body>
  <div class="card">
    <svg class="card__accent-line" viewBox="0 0 1000 571" aria-hidden="true">
      <path d="M0 470 H780 C795 470 795 410 820 410 C840 410 840 470 860 470 H1000"
            fill="none" stroke="var(--accent)" stroke-width="3"/>
    </svg>

    <svg class="card__portrait" viewBox="0 0 250 430" role="img"
         aria-label="Photograph of the dancer mid-leap with one arm outstretched">
      <defs>
        <linearGradient id="portraitTone" x1="0" y1="0" x2="1" y2="1">
          <stop offset="0" stop-color="var(--skin-light)"/>
          <stop offset="0.5" stop-color="var(--skin-mid)"/>
          <stop offset="1" stop-color="var(--skin-dark)"/>
        </linearGradient>
      </defs>
      <rect width="250" height="430" rx="6" fill="url(#portraitTone)"/>
    </svg>

    <div class="card__details">
      <h1 class="card__name">Devon Marsh</h1>
      <p class="card__roles">Dancer Choreographer Instructor Singer/Songwriter</p>
      <p class="card__styles">Ballet-Modern-Urban</p>
      <ul class="card__contact">
        <li>
          <svg class="card__icon" viewBox="0 0 24 24" aria-hidden="true">
            <rect x="2" y="5" width="20" height="14" fill="var(--ink)"/>
            <path d="M3 6.5l9 7 9-7" fill="none" stroke="#fff" stroke-width="1.5"/>
          </svg>
          devonmarsh00@fernpost.com
        </li>
        <li>
          <svg class="card__icon" viewBox="0 0 24 24" aria-hidden="true">
            <path d="M7 2c1 0 2 3 2.5 4.5.3 1-1.5 2-1.5 3 0 2 2.5 5.5 4.5 6.5 1 .5 2-1.5 3-1.2C17 15.3 20 16.5 20 17.5c0 1.5-2 4.5-4 4.5C9 22 2 12 4 5c.5-1.5 2-3 3-3z"/>
          </svg>
          410-582-7146
        </li>
      </ul>
    </div>
  </div>
</body>
</html>
```